Clear tides coaching programme

I need a flyer designed to promote my coaching programme. The programme is designed to help people who are feeling a bit lost in their life, looking for new possiblities or that they want more focus in their goals. It is an intensive programme designed to help people achieve real change in their lives. It is a premium product targeted at senior managers, directors and business leaders. I care passionately about helping people achieve their potential. I would like the design to fit with the logo (attached) and I've drafted the content (also attached). I would like it to be A5 and affordable to print - so not full colour.

```html
<!DOCTYPE html>
<html lang="en">
<head>
<meta charset="utf-8">
<title>Clear tides coaching programme</title>
<link rel="stylesheet" href="https://fonts.googleapis.com/css2?family=Ubuntu:ital,wght@0,400;0,500;0,700;1,400&family=Marcellus&family=Arimo&display=swap">
<style>
  :root{
    --sky-deep:#3f6fc0;
    --sky-mid:#8fb6e6;
    --sky-light:#d9e8f7;
    --paper:#ffffff;
    --headline-blue:#2568c2;
    --purple:#3d2a8c;
    --teal:#1ea598;
    --ink:#111111;
  }
  *{margin:0;padding:0;box-sizing:border-box}
  html,body{width:846px;height:1200px;overflow:hidden;background:var(--paper)}
  .flyer{position:relative;width:846px;height:1200px;overflow:hidden;background:var(--paper);font-family:"Ubuntu",sans-serif}
  .hero-photo{position:absolute;left:0;top:0;width:846px;height:560px;
    background:
      radial-gradient(ellipse 180px 300px at 650px 330px, rgba(255,255,255,.85), rgba(255,255,255,0) 70%),
      linear-gradient(180deg,var(--sky-deep) 0%,var(--sky-mid) 30%,var(--sky-light) 62%,var(--paper) 100%)}
  .quote{position:absolute;left:70px;top:58px;width:720px;color:#fff;font-weight:700;font-size:24px;line-height:31px}
  .quote .author{font-style:italic}
  .headline{position:absolute;left:70px;top:136px;width:600px;color:var(--headline-blue);font-weight:500;font-size:30.5px;line-height:36.5px;letter-spacing:-.6px;
    -webkit-text-stroke:1px #fff;paint-order:stroke fill;text-shadow:0 0 2px #fff,0 0 2px #fff}
  .programme-mark{position:absolute;left:72px;top:400px;width:72px;height:72px;border-radius:50%;background:var(--purple)}
  .programme-details{position:absolute;left:185px;top:325px;width:572px;color:var(--purple);font-style:italic;font-size:18.5px;line-height:26.5px;text-align:justify}
  .promise{position:absolute;left:74px;top:546px;width:694px;color:var(--teal);font-family:"Arimo",sans-serif;font-size:33px;line-height:38.5px;text-align:justify;text-align-last:left;word-spacing:4px}
  .why-title{position:absolute;left:71px;top:682px;color:var(--ink);font-family:"Marcellus",serif;font-size:29px}
  .why-body{position:absolute;left:71px;top:722px;width:694px;color:var(--purple);font-size:20.5px;line-height:31.3px;text-align:justify;text-align-last:left}
  .call{position:absolute;left:0;top:852px;width:846px;text-align:center;color:var(--purple);font-weight:500;font-size:43px}
  .brand{position:absolute;left:0;top:918px;width:846px;display:flex;flex-direction:column;align-items:center;gap:8px}
  .brand-dot{width:52px;height:52px;border-radius:50%;background:var(--teal)}
  .brand-name{color:var(--purple);font-size:17px;font-weight:400;text-transform:uppercase;letter-spacing:.5px}
  .contact-box{position:absolute;left:70px;top:1038px;width:702px;height:125px;background:var(--teal);border-radius:4px;color:#fff;text-align:center;font-weight:700;box-shadow:0 2px 3px rgba(0,0,0,.2)}
  .contact-text{margin-top:13px;font-size:22px;line-height:31px}
  .contact-email{margin-top:7px;font-size:27px;letter-spacing:1.2px}
</style>
</head>
<body>
<main class="flyer">
  <div class="hero-photo" role="img" aria-label="Bright blue sky photograph with a woman in white clothes walking joyfully on the right"></div>

  <p class="quote">“The secret of change is to focus all of your energy not on fighting the old, but on building the new”. <span class="author">ELARA VANCE</span></p>

  <h1 class="headline">Take the first step towards a happier life now by taking up your own, personally tailored ‘Clear tides’ coaching programme.</h1>

  <div class="programme-mark" aria-hidden="true"></div>
  <p class="programme-details">The Clear tides programme consists of 6 face to face confidential coaching sessions of 60-90 minutes.<br>Each session is carefully designed around you, your needs and goals.<br>You will also benefit from bespoke email support in between sessions, development feedback, recommended resources to support your journey and a bespoke action plan.</p>

  <p class="promise">This programme will help you achieve your goals and increase your satisfaction with your work and home life.</p>

  <h2 class="why-title">Why work with me?</h2>
  <p class="why-body">I’m a coach and transformational leader with a decade of experience in delivering better results for individuals, organisations and customers.&nbsp; I’m passionate about helping people achieve their potential and find new possibilities.</p>

  <p class="call">Take your first step now</p>

  <div class="brand">
    <span class="brand-dot" aria-hidden="true"></span>
    <span class="brand-name">Reaching Further</span>
  </div>

  <section class="contact-box">
    <p class="contact-text">Contact me today and book a complimentary 15 minute phone<br>or Linkwave consultation by emailing me</p>
    <p class="contact-email">reachingfurther@mailpost.com</p>
  </section>
</main>
</body>
</html>
```